Specialty Chemical Product Line Card Revamp

I need a new digital brochure for our product catalog of various chemicals. This will be sent to my customers as a digital file or printed on flat paper (not a folded brochure). I have included the OLD brochure (Tobin Chemical Line Card document) and the new categories that I want used instead (Line Card Categories document). I also included our logo and other photos. I would like the new brochure to be more modern and attention-grabbing

Target Market(s)

Product Manufacturers

Industry/Entity Type

Chemical Product

Font styles to use
Serif
Sans Serif

Requirements
Must have
• Product Category Headers. Company Logo
Nice to have
• Incorporate the attached photos. Use similar colors as the logo. Fit on 2 pages
Should not have
• Cannot be more than 3 pages.

```html
<!DOCTYPE html>
<html lang="en">
<head>
<meta charset="utf-8">
<title>Tobin Chemical – Product Line Card</title>
<link href="https://fonts.googleapis.com/css2?family=Open+Sans:wght@400&family=Roboto+Condensed:wght@300;400&display=swap" rel="stylesheet">
<style>
  :root {
    --green: #7bb45a;
    --purple: #46388c;
    --purple-dark: #342a73;
    --panel: #f1f1f2;
    --ink: #33343a;
    --page: #ffffff;
    --backdrop: #dfe3e0;
    --shadow: #b8bcba;
  }
  * { box-sizing: border-box; }
  html, body {
    margin: 0;
    width: 1200px;
    height: 2616px;
    overflow: hidden;
    background: var(--backdrop);
  }
  .sheet {
    position: absolute;
    left: 160px;
    width: 880px;
    height: 1210px;
    background: var(--page);
    box-shadow: 16px 16px 0 var(--shadow);
    overflow: hidden;
  }
  .sheet--front { top: 60px; }
  .sheet--back { top: 1346px; }
  .sheet svg { position: absolute; left: 0; display: block; }
  .brand {
    position: absolute;
    left: 30px;
    top: 40px;
    margin: 0;
    display: flex;
    align-items: center;
    gap: 12px;
    font: 400 30px/1 "Roboto Condensed", sans-serif;
    color: var(--ink);
    letter-spacing: 0.5px;
  }
  .brand-mark {
    width: 18px;
    height: 18px;
    background: var(--green);
  }
  .panel {
    position: absolute;
    background: var(--panel);
    padding-bottom: 12px;
  }
  .tab {
    display: inline-block;
    margin: 0 0 14px;
    padding: 9px 34px 8px 16px;
    background: var(--green);
    color: #fff;
    font: 300 18px/1 "Roboto Condensed", sans-serif;
    text-transform: uppercase;
    white-space: nowrap;
    clip-path: polygon(0 0, 100% 0, calc(100% - 22px) 100%, 0 100%);
  }
  .tab--lg { font-size: 22px; padding: 9px 40px 8px 14px; }
  .items {
    margin: 0;
    padding: 0 10px 0 32px;
    font: 400 10px/12px "Open Sans", sans-serif;
    color: var(--ink);
  }
  .items li { white-space: nowrap; }
  .items li::marker { font-size: 8px; }
  .cols {
    display: grid;
    grid-template-columns: 162px 186px 186px 1fr;
    padding-left: 6px;
  }
  .cols .items { padding-right: 4px; font-size: 9.5px; }
  .cols--two { grid-template-columns: 1fr 1fr; padding-left: 0; }
</style>
</head>
<body>

<!-- Page one -->
<section class="sheet sheet--front">
  <svg width="880" height="460" viewBox="0 0 880 460" style="top:0">
    <defs>
      <linearGradient id="roadScene" x1="0" y1="0" x2="0" y2="1">
        <stop offset="0" stop-color="#8cc8d0"/>
        <stop offset="0.32" stop-color="#6d9a72"/>
        <stop offset="0.6" stop-color="#3f4f92"/>
        <stop offset="1" stop-color="#7f868a"/>
      </linearGradient>
    </defs>
    <polygon points="398,0 880,0 880,460 0,460 0,126 352,126" fill="url(#roadScene)" role="img" aria-label="Photo of a blue delivery truck and trailer on a highway beside green hills"/>
    <rect x="0" y="106" width="336" height="14" fill="var(--purple)"/>
    <polygon points="364,0 394,0 350,122 320,122" fill="var(--green)"/>
    <polygon points="0,440 40,440 24,456 0,456" fill="var(--green)"/>
  </svg>
  <h1 class="brand"><span class="brand-mark"></span>Tobin Chemical</h1>

  <div class="panel" style="left:66px;top:318px;width:752px;height:288px">
    <h2 class="tab" style="min-width:168px">Solvents</h2>
    <div class="cols">
      <ul class="items">
        <li>Acetate, N-butyl</li><li>Acetate, N-propyl</li><li>Acetone</li><li>Aliphatic Solvents</li><li>Amyl Acetate</li><li>Aromatic Solvents</li><li>Butyl Acetate</li><li>Cyclohexane</li><li>Cyclohexanone</li><li>DB Acetate</li><li>DE Acetate</li><li>Disobutyl Ketone (DIBK)</li><li>Dimethylformamide</li><li>EB Acetate</li><li>Ethyl Acetate</li><li>Ethyl Ether, Reagent</li><li>Ethylene Dichloride</li>
      </ul>
      <ul class="items">
        <li>Heptane</li><li>Hexane</li><li>Isobutyl Acetate</li><li>Isophorone</li><li>Isopropyl Acetate</li><li>Ketones</li><li>Methyl Amyl Ketone</li><li>Methyl Glycotol (DM)</li><li>Methyl Solvenol (EM)</li><li>Methyl Ethyl Ketone (MEK)</li><li>Methyl Isoamyl Ketone</li><li>Methyl Isobutyl Ketone (MIBK)</li><li>Methyl Salicylate</li><li>Methylene Chloride</li><li>Mineral Spirits, Low odor</li><li>Mineral Spirits, Odorless</li>
      </ul>
      <ul class="items">
        <li>Mineral Spirits, Rule 66</li><li>Mineral Spirits, Stoddard Solvent</li><li>n-Butyl Pyrrolidone</li><li>n-Propyl Bromide</li><li>Perchloroethylene</li><li>Petroleum Ether</li><li>PM Acetate</li><li>FastDri Solvent</li><li>Sodium Acetate</li><li>Solvent 100</li><li>Solvent 142</li><li>Solvent 150</li><li>Formic Acid</li><li>Glacial Acetic Acid</li><li>Gluconic Acid</li><li>Glycolic Acid</li>
      </ul>
      <ul class="items">
        <li>Hydrochloric Acid</li><li>Hydrochloric Acid Reagent</li><li>Hydrofluoric Acid</li><li>Hydrofluosilicic Acid 25%</li><li>Lactic Acid</li><li>Muriatic Acid 18°, 20°, 22°</li><li>Muriatic Acid, Inhibited</li><li>Nitric Acid</li><li>Nitric Acid, Reagent</li><li>Oxalic Acid</li><li>Phosphoric Acid 75%, 85%, Tech</li><li>Phosphoric Acid, Reagent</li><li>Sorbic Acid</li><li>Sulfamic Acid</li><li>Sulfuric Acid 66°</li><li>Sulfuric Acid, Reagent</li>
      </ul>
    </div>
  </div>

  <div class="panel" style="left:66px;top:616px;width:218px;height:252px">
    <h2 class="tab" style="min-width:150px">Oils</h2>
    <ul class="items" style="padding-left:48px">
      <li>Naphthenic Base Oil</li><li>D-Limonene</li><li>Kerosene</li><li>Mineral Seal Oil</li><li>Mop Oil</li><li>Naphtha, V M &amp;P</li><li>Naphthenic Oils</li><li>Pine Oil</li><li>V M &amp; P Naphtha</li><li>Vanishing Oil</li><li>Way Lubricants</li><li>White Kerosene</li><li>White Oils</li>
    </ul>
  </div>

  <div class="panel" style="left:66px;top:880px;width:218px;height:290px">
    <h2 class="tab" style="min-width:178px">Metals &amp; Salts</h2>
    <ul class="items" style="padding-left:42px">
      <li>Aluminum Chloride</li><li>Aluminum Sulfate</li><li>Bicarbonate of Soda</li><li>Borax 5 mol, pentahydrate</li><li>Cadmium Oxide</li><li>Calcium Acetate</li><li>Calcium Boride</li><li>Calcium Chloride, liquid</li><li>Calcium Nitrate</li><li>Zinc Anodes</li><li>Zinc Chloride</li><li>Zinc Cyanide</li><li>Zinc Oxide</li>
    </ul>
  </div>

  <div class="panel" style="left:296px;top:616px;width:270px;height:554px">
    <h2 class="tab" style="min-width:150px">Solids</h2>
    <ul class="items" style="padding-left:28px">
      <li>Activated Carbon</li><li>Anhydrous Ammonia</li><li>Aluminum Sulfate</li><li>Barium Carbonate</li><li>Bicarbonate of Soda</li><li>CCH Granular 65% (GCH)</li><li>Calcium Boride</li><li>Calcium Chloride, flake or pellets</li><li>Calcium Nitrate</li><li>Caustic Potash, flake</li><li>Caustic Soda, beads or flake</li><li>Citric Acid, USP</li><li>Copper Cyanide</li><li>Copper Sulfate, crystal</li><li>Dipotassium Phosphate, FCC</li><li>Disodium Phosphate, FCC</li><li>Epsom Salts</li><li>Manganese Sulfate, dry</li><li>Muriate of Potash</li><li>Nickel Chloride, dry</li><li>Nickel Sulfate, salt</li><li>Floor Dri Adsorbent</li><li>Pelacal</li><li>Rochelle Salts</li><li>Rock Salt</li><li>Sodium Bisulfate, Anhy G.B.S.</li><li>Sodium Citrate, USP granular</li><li>Sodium Metasilicate, Anhy. Drysil</li><li>Sodium Sulfate, Anhydrous</li><li>Sodium Thiosulate, dry</li><li>Sodium Tripolyphosphate, Anhy. Gran. Lite</li><li>Sodium Tripolyphosphate, Anhy. Gran. Tech</li><li>Tetra Potassium Pyro Phosphate, Gran. Tech</li><li>Zinc Dust</li>
    </ul>
  </div>

  <div class="panel" style="left:578px;top:616px;width:240px;height:200px">
    <h2 class="tab" style="padding-right:30px">Ammonium Compounds</h2>
    <ul class="items" style="padding-left:26px">
      <li>Ammonium Bicarbonate</li><li>Ammonium Chloride, Treated or Untreated</li><li>Ammonium Bifluoride</li><li>Ammonium Hydroxide 21, 26</li><li>Ammonium Hydroxide, Reagent</li><li>Ammonium Nitrate</li><li>Ammonium Persulfate</li><li>Ammonium Sulfate</li><li>Anhydrous Ammonia</li><li>Monoammonium Phosphate</li>
    </ul>
  </div>

  <div class="panel" style="left:578px;top:826px;width:240px;height:344px">
    <h2 class="tab" style="min-width:196px">By Function</h2>
    <ul class="items" style="padding-left:26px">
      <li>Antifoams</li><li>Antifreeze</li><li>Blanket/Roller Wash</li><li>Chelating Agents</li><li>Chlorinated Solvents</li><li>Cleaners, Floor, Metal, Soak, Steam</li><li>Coolants</li><li>Corrosion Inhibitors</li><li>Cutting Oils</li><li>Dechlorinators</li><li>Defoamers</li><li>Degreasing Solvents</li><li>De-Icers</li><li>Descaling Acid</li><li>Electro Cleaners</li><li>Tetrahydrafuran</li><li>Toluene</li><li>Trichloroethylene</li><li>Typewash</li><li>Xylene</li>
    </ul>
  </div>

  <svg width="880" height="34" viewBox="0 0 880 34" style="top:1176px">
    <polygon points="0,2 560,2 540,18 0,18" fill="var(--green)"/>
    <polygon points="548,2 880,2 880,34 512,34" fill="var(--purple-dark)"/>
  </svg>
</section>

<!-- Page two -->
<section class="sheet sheet--back">
  <svg width="880" height="290" viewBox="0 0 880 290" style="top:0">
    <defs>
      <linearGradient id="labScene" x1="0" y1="0" x2="1" y2="1">
        <stop offset="0" stop-color="#8d7fc6"/>
        <stop offset="0.55" stop-color="#b9aee0"/>
        <stop offset="1" stop-color="#e6e1f4"/>
      </linearGradient>
    </defs>
    <polygon points="0,0 880,0 880,286 560,286 560,212 0,212" fill="url(#labScene)" role="img" aria-label="Photo of laboratory glassware filled with violet liquid"/>
  </svg>

  <div class="panel" style="left:42px;top:170px;width:250px;height:256px">
    <h2 class="tab" style="min-width:184px">Miscellaneous</h2>
    <ul class="items" style="padding-left:28px">
      <li>All Purpose Cleaner</li><li>Bleach</li><li>Polywax</li><li>Caustic Soda Liquid 50%, Diaphragm Grade</li><li>Caustic Soda Liquid 50%, Membrane Grade</li><li>Distilled Water</li><li>Frostguard</li><li>Thermaflo</li><li>Formaldehyde 37%</li><li>Hydrogen Peroxide, Tech, Food Grade</li><li>Silkal (Potassium Silicate)</li><li>Swift Dry</li><li>Soaps</li><li>Polyols</li><li>Urea</li><li>Winshield Washer Solvent</li>
    </ul>
  </div>

  <div class="panel" style="left:42px;top:436px;width:250px;height:256px">
    <h2 class="tab tab--lg" style="min-width:210px">Miscellaneous</h2>
    <ul class="items" style="padding-left:28px">
      <li>All Purpose Cleaner</li><li>Bleach</li><li>Polywax</li><li>Caustic Soda Liquid 50%, Diaphragm Grade</li><li>Caustic Soda Liquid 50%, Membrane Grade</li><li>Distilled Water</li><li>Frostguard</li><li>Thermaflo</li><li>Formaldehyde 37%</li><li>Hydrogen Peroxide, Tech, Food Grade</li><li>Silkal (Potassium Silicate)</li><li>Swift Dry</li><li>Soaps</li><li>Polyols</li><li>Urea</li><li>Winshield Washer Solvent</li>
    </ul>
  </div>

  <div class="panel" style="left:42px;top:702px;width:250px;height:460px">
    <h2 class="tab tab--lg" style="min-width:190px">Alcohols</h2>
    <ul class="items" style="padding-left:28px">
      <li>Butanol</li><li>Cyclohexanol</li><li>Denatured Alcohol</li><li>Diacetone Alcohol</li><li>DBE</li><li>Diethylene Glycol</li><li>Dipropylene Glycol</li><li>Frostguard</li><li>Thermaflo SR-1</li><li>Ethyl Alcohol 190 Proof</li><li>Ethyl Alcohol 200 Proof</li><li>Ethylene Glycol</li><li>Glycerine</li><li>Glycol Ether Acetates</li><li>Hexylene Glycol</li><li>Isobutyl Alcohol</li><li>Isopropyl Alcohol</li><li>Methanol</li><li>Methyl Amyl Alcohol</li><li>n-Butyl Alcohol</li><li>n-Propyl Alcohol</li><li>Polyethylene Glycols</li><li>Propylene Glycol, Industrial</li><li>Propylene Glycol, USP</li><li>Secondary Butyl Alcohol</li><li>Sorbitol</li><li>Surfanols</li><li>Teiethylene Glycol</li>
    </ul>
  </div>

  <div class="panel" style="left:306px;top:170px;width:268px;height:992px">
    <h2 class="tab tab--lg" style="min-width:240px">Sodium Compounds</h2>
    <ul class="items" style="padding-left:26px">
      <li>Disodium Phosphate, FCC</li><li>Monosodium Phosphate</li><li>Sodium Acetate</li><li>Sodium Benzoate</li><li>Sodium Bichromate</li><li>Sodium Bisulfate, Anhy G.B.S.</li><li>Sodium Bisulfite, liquid</li><li>Sodium Bicarbonite</li><li>Sodium Bifluoride</li><li>Sodium Canide</li><li>Sodium Chlorate</li><li>Sodium Citrate, USP granular</li><li>Sodium Fluoride</li><li>Sodium Gluconate</li><li>Sodium Hexametaphosphate, Tech</li><li>Sodium Hexametaphosphate, Food grade</li><li>Sodium Hydrosulfite</li><li>Sodium Hypochlorite</li><li>Sodium Metasilicate, Anhy. Drysil</li><li>Sodium Metasilicate, Pent. Crystasil</li><li>Sodium Molybdate</li><li>Sodium Nitrate</li><li>Sodium Nitrite</li><li>Sodium Percarbonate</li><li>Sodium Permanganate</li><li>Sodium Persulfate</li><li>Sodium Acid Pyrophosphate</li><li>Sodium Silicate</li><li>Sodium Silicofluoride</li><li>Sodium Sulfide</li><li>Sodium Sulfate</li><li>Sodium Sulfate, Anhydrous</li><li>Sodium Thiosulate, liquid or dry</li><li>Sodium Tripolyphosphate, Anhy. Gran. Lite</li><li>Sodium Tripolyphosphate, Anhy. Gran. Tech</li><li>Tetra Sodium Pyro Phosphate, FCC</li><li>Trisodium Phosphate</li><li>Filter Powders</li><li>Floor Adsorbents</li><li>Foam Control</li><li>Form Oils</li><li>Gear Oils</li><li>Heat Transfer Fluids</li><li>Hydraulic Fluids</li><li>Inhibited Glycol Fluids</li><li>Lacquer Reducers</li><li>Lacquer Thinners</li><li>Laboratory Chemicals</li><li>Metal Cleaners</li><li>Metal Conditioners</li><li>Metalworking Lubricants</li><li>Nonionic Surfactants</li><li>Paint Strippers</li><li>Paint Thinners</li><li>Process Oils</li><li>Reagent Acids</li><li>Reagent Solvents</li><li>Rubber Rejuvenator</li><li>Rust Proofers</li><li>Safety Absorbent</li><li>Safety Solvents</li><li>Soak Cleaners</li><li>Soluble Oils</li><li>Steam Cleaners</li><li>Surfactants</li><li>Synthetic Coolants</li><li>Thinners</li><li>Waste Water Treatment Solutions</li><li>Water Soluble Oils</li><li>Wetting Agents</li>
    </ul>
  </div>

  <div class="panel" style="left:588px;top:170px;width:250px;height:94px">
    <h2 class="tab" style="min-width:156px">Amines</h2>
    <div class="cols cols--two">
      <ul class="items" style="padding-left:22px"><li>Cyclohexylamine</li><li>DEA 99%</li></ul>
      <ul class="items" style="padding-left:14px"><li>Diethylamine</li><li>Diethylethanolamine</li></ul>
    </div>
  </div>

  <div class="panel" style="left:588px;top:274px;width:250px;height:888px">
    <h2 class="tab" style="min-width:196px">Acids</h2>
    <ul class="items" style="padding-left:44px">
      <li>Acetic Acid 28%, 56%, 75%, 80%</li><li>Acetic Acid Glacial 99.5%</li><li>Acetic Acid, Reagent</li><li>Boric Acid</li><li>Chromic Acid</li><li>Citric Acid, USP</li><li>Citric Acid, Liquid</li><li>EDTA (Chelate)</li><li>Fluoboric Acid 48-50%</li><li>Chlorine, gas, liquid or dry</li><li>Copper Anodes</li><li>Copper Cyanide</li><li>Copper Sulfate, Crystal</li><li>DDBSA</li><li>Dipotassium Phosphate, FCC</li><li>Epsom Salts</li><li>Ferric Chloride DWG</li><li>Ferric Sulfate</li><li>Ferrous Sulfate (Copperas)</li><li>Iron Phosphates</li><li>Lime, hydrated</li><li>Lithium Carbonate</li><li>Magnesium Chloride</li><li>Magnesium Hydroxide</li><li>Magnesium Oxide</li><li>Magnesium Sulfate</li><li>Manganese Carbonate</li><li>Manganese Sulfate, liquid or dry</li><li>Monoaluminum Phosphate</li><li>Monopotassium Phosphate</li><li>Nickel Acetate</li><li>Nickel Anodes</li><li>Nickel Chloride, solution</li><li>Nickel Fluoborate</li><li>Nickel Sulfate, solution</li><li>Phosphates</li><li>Polyphosphates</li><li>Potassium Copper Cyanide</li><li>Potassium Alum</li><li>Potassium Carbonate</li><li>Potassium Chloride</li><li>Potassium Cyanide</li><li>Potassium Permanganate</li><li>Rochelle Salts</li><li>Rock Salt</li><li>Soda Ash</li><li>Soap</li><li>Stannous Fluoborate,solution</li><li>Stannous Sulfate</li><li>Sulfur</li><li>Sulfur Dioxide</li><li>Tetra Potassium Pyro Phosphate, FCC</li><li>Tolytriazole</li><li>Tricalcium Phosphate</li><li>Glassphos</li><li>Dimethyl Ethanolamine</li><li>Ethylenediamine</li><li>Monoethanolamine</li><li>Morpholine</li><li>Triethylolamine 85%, 99%</li><li>Triethylamine</li>
    </ul>
  </div>

  <svg width="880" height="34" viewBox="0 0 880 34" style="top:1176px">
    <polygon points="0,2 560,2 540,18 0,18" fill="var(--green)"/>
    <polygon points="548,2 880,2 880,34 512,34" fill="var(--purple-dark)"/>
  </svg>
</section>

</body>
</html>
```